R J Penn Accounting & SMSF Auditing needs a Web Site Design

I need some examples of what a web design can look like for my business.
The business name is above and I have already registered a domain name of www.penn-smsf.com.au
I have attached my current letterhead and business cards and would like to maintain these colours basically Red on White with some black

```html
<!DOCTYPE html>
<html lang="en">
<head>
<meta charset="utf-8">
<title>R.J. Penn Accounting &amp; SMSF Auditing</title>
<link href="https://fonts.googleapis.com/css2?family=Questrial&family=Maven+Pro:wght@400;700&family=Arimo:wght@400;700&family=Open+Sans:wght@400;600&display=swap" rel="stylesheet">
<style>
:root{
  --red:#c8102e;
  --red-dark:#7a0c1c;
  --black:#0a0a0a;
  --ink:#222;
  --body:#555;
  --rule:#c8c8c8;
  --white:#fff;
}
*{margin:0;padding:0;box-sizing:border-box}
html,body{width:1200px;height:1134px;overflow:hidden;background:var(--white)}
body{position:relative;font-family:'Arimo',Arial,sans-serif;color:var(--body)}
.header-band{position:absolute;left:0;top:0;width:1200px;height:146px;background:linear-gradient(#fff,#ececec)}
.wrap{position:absolute;left:149px;top:0;width:902px;height:1134px}
.brand{position:absolute;left:1px;top:18px;white-space:nowrap;font-family:'Questrial',sans-serif}
.brand-name{color:var(--red);font-size:27px;font-weight:400;letter-spacing:.5px}
.brand-tag{color:#333;font-size:27px;margin-left:6px}
.brand-sub{position:absolute;left:156px;top:41px;font-size:18px;color:#333}
.phone{position:absolute;right:2px;top:47px;display:flex;align-items:center;gap:4px;font:700 23px 'Arimo',Arial,sans-serif;color:#333}
.nav{position:absolute;left:0;top:105px;width:902px;height:42px;background:linear-gradient(#3a3a3a,#000 60%);border-radius:3px;display:flex;align-items:center}
.nav a{color:#fff;text-decoration:none;font-size:13.5px;height:42px;line-height:42px;padding:0 24px;border-right:1px solid #444}
.nav a:first-child{padding:0 24px 0 27px}
.search{position:absolute;right:7px;top:10px;width:194px;height:23px;background:#fff;font:13px 'Arimo',sans-serif;color:#777;padding:4px 7px}
.search svg{position:absolute;right:6px;top:4px}
.slider{position:absolute;left:0;top:170px;width:902px;height:300px;background:linear-gradient(110deg,#f0d9cf 0%,#e8e6e4 40%,#dcdad8 65%,#e9c8b6 85%,#d8d8da 100%)}
.cap{position:absolute;color:#fff;font-size:22px;padding:2px 10px}
.cap-1{left:33px;top:190px;background:rgba(20,20,20,.88)}
.cap-2{left:134px;top:223px;background:rgba(200,16,46,.9)}
.dots{position:absolute;right:14px;top:272px;width:77px;height:18px;background:rgba(20,20,20,.85);border-radius:4px;display:flex;justify-content:space-evenly;align-items:center}
.dots span{width:10px;height:10px;border-radius:50%;background:#fff}
.dots span.on{background:var(--red)}
.features{position:absolute;left:0;top:502px;width:902px;height:158px;display:flex;border-radius:3px;overflow:hidden}
.feature{flex:1;padding:16px 22px;color:#fff;background:linear-gradient(var(--red),var(--red-dark));border-left:1px solid #8e0d20}
.feature.dark{background:linear-gradient(#4a4a4a,#000);border:none}
.feature h3{font:400 21px 'Maven Pro',sans-serif;margin-bottom:11px}
.feature h3 b{font-weight:700}
.feature p{font-size:12.8px;line-height:20.6px;text-align:justify;letter-spacing:.3px}
.feature .more{font-weight:700;letter-spacing:.6px;font-size:13px}
.welcome{position:absolute;left:-2px;top:699px;font:400 27px 'Maven Pro',sans-serif;color:#222;white-space:nowrap}
.welcome b{font-weight:700}
.welcome small{font-size:22px;margin-left:6px}
.intro{position:absolute;left:1px;top:752px;width:577px;font-size:13.3px;line-height:20.6px;text-align:justify}
.intro p{margin-bottom:20.6px}
.btn{position:absolute;left:1px;top:991px;width:92px;height:33px;background:linear-gradient(#d41a36,#8a0c1e);border:1px solid #700a18;border-radius:3px;color:#fff;font-size:13.5px;line-height:31px;text-align:center}
.featured{position:absolute;left:628px;top:699px;width:274px}
.featured h2{font:400 27px 'Maven Pro',sans-serif;color:#222;margin-bottom:14px}
.featured h2 b{font-weight:700}
.featured li{list-style:none;height:28.1px;line-height:26px;border-bottom:1px dotted #aaa;font:12px/26px 'Open Sans',sans-serif;color:#555;padding-left:20px;position:relative}
.featured li::before{content:"";position:absolute;left:1px;top:10px;border-left:4px solid #555;border-top:3px solid transparent;border-bottom:3px solid transparent}
.featured li:last-child{border:none}
.footer{position:absolute;left:0;top:1069px;width:902px;height:42px;background:linear-gradient(#3a3a3a,#000 60%);border-radius:3px;color:#fff;font-size:12px;display:flex;align-items:center;padding:0 19px}
.footer .sep{margin:0 10px}
.follow{margin-left:auto;display:flex;align-items:center;gap:9px}
.follow i{width:21px;height:21px;border-radius:2px;display:inline-block}
.sq-blue{background:#3b5998}.sq-sky{background:#29a9e1}
</style>
</head>
<body>
<div class="header-band"></div>
<div class="wrap">
  <div class="brand"><span class="brand-name">R.J. Penn</span><span class="brand-tag">Accounting &amp; SMSF Auditing</span>
    <div class="brand-sub">Penrose Penn Pty Ltd T/A</div></div>
  <div class="phone">
    <svg width="24" height="32" viewBox="0 0 24 32" aria-hidden="true"><path d="M16 2c-9 3-12 17-5 27l3-2c-5-8-4-17 4-21z" fill="#c8102e"/><path d="M17 1l4-1 2 5-4 2z" fill="#c8102e"/></svg>
    03 5550 1287</div>
  <nav class="nav">
    <a>Home</a><a>About Us</a><a>Our Services</a><a>Our Expertise</a><a>Contact Us</a>
    <div class="search">Search Here<svg width="16" height="15" viewBox="0 0 16 15" aria-hidden="true"><circle cx="6" cy="6" r="4.5" fill="none" stroke="#666" stroke-width="2"/><path d="M9.5 9.5l5 4" stroke="#666" stroke-width="2.5"/></svg></div>
  </nav>
  <div class="slider" role="img" aria-label="Photo of hands working over financial charts with a pen and laptop">
    <div class="cap cap-1">Dultricies phaetrades magnasonec</div>
    <div class="cap cap-2">Accumsan malesuada nec simet</div>
    <div class="dots"><span></span><span class="on"></span><span></span><span></span></div>
  </div>
  <div class="features">
    <div class="feature dark"><h3><b>Accounting</b> Service</h3><p>Lorem ipsum dolor sit amet, consec tetuer adipiscing elit. Praesent vestibu lum mo lestie lacusenean.<br><span class="more">Read More</span></p></div>
    <div class="feature"><h3><b>Business</b> Consulting</h3><p>Lorem ipsum dolor sit amet, consec tetuer adipiscing elit. Praesent vestibu lum mo lestie lacusenean.<br><span class="more">Read More</span></p></div>
    <div class="feature"><h3><b>Unlimited</b> Support</h3><p>Lorem ipsum dolor sit amet, consec tetuer adipiscing elit. Praesent vestibu lum mo lestie lacusenean.<br><span class="more">Read More</span></p></div>
  </div>
  <h1 class="welcome">Welcome to <b>R.J. Penn</b> <small>Accounting &amp; SMSF Auditing</small></h1>
  <div class="intro">
    <p>Mmonlase dusce hertserro loremmal esuada odio fertase orbinunc diolse kertase gravida atcursus alor aecenas atique orciacsem. Dultricies phaetrades magnasonec accumsan malesuada nec simet erorem idolor sit aconse meserda lerosea sneuctus ctetuer adipiscing mergase ferdesel aerment laoreet aliquam. Aliquam erat volutpat. Duis ac turpinteger rutrum ante eu lacus. Kahaetrades magnasonec accumsan malesuada nec simet erorem idolor sit acons.</p>
    <p>Mmonlase dusce hertserro loremmal esuada odio fertase orbinunc diolse kertase gravida atcursus alor aecenas atique orciacsem. Dultricies phaetrades magnasonec accumsan malesuada nec simet erorem idolor sit aconse meserda lerosea sneuctus ctetuer adipiscing mergase ferdesel aerment laoreet aliquam. Aliquam erat volutpat.</p>
  </div>
  <div class="btn">Read More</div>
  <div class="featured">
    <h2><b>Featured</b> Services</h2>
    <ul>
      <li>Natoque artusmiase kerode nasery</li>
      <li>Keriase malesuada odiorbi kunioravida</li>
      <li>Mertasede aerta</li>
      <li>Ferode monlase dusmia nerasen</li>
      <li>Cursus necluctus alorem ecenas trise</li>
      <li>Useorci ac semis ultricies pharetra</li>
      <li>Magna onec accumsan malesu</li>
      <li>Lasada nec sit amet erorem ipsum</li>
      <li>Dolor sit aconsectetuer adipi</li>
      <li>Acing el auris ferment aoret aliquam</li>
    </ul>
  </div>
  <footer class="footer">
    <span>© R.J. Penn Accounting &amp; SMSF Auditing 2014</span><span class="sep">|</span><span>Privacy policy</span><span class="sep">|</span><span>Terms and Conditions</span>
    <div class="follow">Follow Us <i class="sq-blue"></i><i class="sq-sky"></i></div>
  </footer>
</div>
</body>
</html>
```